Laboratory Pain Managment Brochure

I want a simple easy to read brochure for doctors. My toxicology lab is in the pain management arena. We provide urine drug monitoring to ensure patients are taking their medication properly. I would like a few photos of adults, doctors, nurses and a happy family. Also, feel free to add a logo that would describe this type of testing

Running theme like " Successfully serving North Dakota since 1996 "

Cover Page # 1

Brilliant photo with Corvella Diagnostics

Would like a running theme of being Corvella being a North Dakota based lab

Page # 2

Corvella Labs has been successfully serving North Dakota since 1996. Dr. Gavin Tellemy, President of Corvella Lab, has over 25 years of medical experience doing research for Brindle University and The University of Parkmoor. In addition, he has worked with clinics giving him a comprehensive understanding of drug testing. It is Corvella Lab mission to supply the best service for our costumers by understanding their needs so they can provide the best possible patient care.

Corvella Features:
•24 – 48 Hour Turnaround Time
•Customer Satisfaction is Our Number 1 Priority
•Capable of Billing all Major Insurance Companies
•Thorough Drug Testing Capabilities Including K2/Spice testing
•Apply Lean Process Control to Supply the best Quality of Analysis
•Easy and Convenient Web-based Interface
•Easy and Customizable Reporting
-The Vexlo is state of the art technology that uses ion entrapment to give better quantitative results. This gives us the ability to detect for more drugs at a higher accuracy.

Why test: Page # 2

Why Monitor Prescription Drug Usage? Prescription drug abuse is the use of medication without a prescription, in a way other than prescribed, or for the experience or feeling elicited. According to several national surveys, prescription medications, such as those used to treat pain, attention deficit disorders, and anxiety, are being abused at a rate second only to marijuana among illicit drug users. The consequences of this abuse have been steadily worsening, reflected in increased treatment admissions, emergency room visits, and overdose deaths.

Can you tell if your patient is taking his/her medication properly?
Even though monitoring your patients behavior is important it is not adequate to know if the patient is misusing their medications. Monitoring the patients behavior as well as drug monitoring testing will give you the most insight into your patients drug usage.

There are many reasons why pain patients may not be taking their medication as prescribed:
•Due to fear of addiction will not take the medication.
•Compulsive use because of addiction.
•Sell the medication to someone else for profit.
•Abuse the medication intentionally

FWRAB's Dosage Integrity Safeguard Plan
The 2011 Dosage Integrity Safeguard Plan expands upon the Harlow Administration's Federal Substance Oversight Agenda and includes action in four major areas to reduce prescription drug abuse:

•Education. A crucial first step in tackling the problem of prescription drug abuse is to educate parents, youth, and patients about the dangers of abusing prescription drugs, while requiring prescribers to receive education on the appropriate and safe use, and proper storage and disposal of prescription drugs.
•Monitoring. Implement prescription drug monitoring programs (PDMPs) in every state to reduce “doctor shopping” and diversion, and enhance PDMPs to make sure they can share data across states and are used by healthcare providers.
•Proper Medication Disposal. Develop convenient and environmentally responsible prescription drug disposal programs to help decrease the supply of unused prescription drugs in the home.
•Enforcement. Provide law enforcement with the tools necessary to eliminate improper prescribing practices and stop pill mills.

References
1.(2011, October). Retrieved November 2012, from BSRC: Bureau of Substance Research Councils: http://www.example-substancebureau.test/sites/default/files/rrdosage.pdf
2.Commun Care Rev. 2009 Aug;12(4):185-90. doi: 10.1089/pop.2009.0015
3. http://www.example-federaloffice.test/fwrab/dosage-integrity

Page # 3 a list of all four panels we offer....... see attachment and use title of panel in the tabs at the bottom of the excel sheet

Back cover Page # 4 ..... brilliant picture..... North Dakota based lab

Corvella Diagnostics, Inc.
482 Larkfield Ave. E
Williston, ND 58934
ph: (701) 555-0143
www.corvellalab.test

I have removed one stat and added another...... please see the references section

Thank you

Target Market(s)

Pain Managment doctors, internal medicine doctors, general practioners, nuerologist, rehab centers, detox facility, hospitals, just about any doctor that prescribes schedule 2 narcotics

Industry/Entity Type

Healthcare

Requirements
Must have
• Back page I want the family picture with a caption reading

We view your patients like family

```html
<!DOCTYPE html>
<html lang="en">
<head>
<meta charset="utf-8">
<title>Corvella Diagnostics Brochure</title>
<link rel="stylesheet" href="https://fonts.googleapis.com/css2?family=Open+Sans:wght@400;600;700&display=swap">
<style>
  :root {
    --bg: #d9e2c8;
    --band: #b9cbd6;
    --ink: #1d232a;
    --accent: #2b8fd0;
    --white-coat: #f3f5f7;
    --bench-grey: #c7d3db;
    --glass-blue: #7fb3d4;
    --tube-green: #4f9a6a;
    --shirt-blue: #8fa9cc;
  }
  * { box-sizing: border-box; margin: 0; padding: 0; }
  html, body { width: 1200px; height: 960px; overflow: hidden; }
  body {
    background: var(--bg);
    font-family: "Open Sans", Arial, sans-serif;
    color: var(--ink);
    position: relative;
  }
  .page {
    position: absolute;
    top: 182px;
    width: 460px;
    height: 595px;
    background: var(--band);
    box-shadow: 0 6px 18px rgba(60, 70, 50, 0.25);
    overflow: hidden;
  }
  .page--inside { left: 110px; display: flex; flex-direction: column; }
  .page--cover { left: 630px; }

  .inside-top-band { height: 26px; flex: none; }

  .photo { width: 100%; flex: none; }
  .photo--tubes {
    height: 150px;
    background:
      linear-gradient(180deg, rgba(255,255,255,0) 55%, rgba(79,154,106,0.55) 75%, rgba(79,154,106,0.2) 92%, rgba(255,255,255,0) 100%),
      linear-gradient(90deg, var(--white-coat) 0%, #e4ebe6 60%, #d9dcd6 100%);
  }
  .photo--office {
    height: 70px;
    margin-top: auto;
    background: linear-gradient(90deg, var(--white-coat) 0%, #e9edf1 45%, var(--shirt-blue) 80%, #dfe4ea 100%);
  }
  .photo--lab {
    position: absolute;
    top: 158px;
    left: 0;
    height: 288px;
    background:
      linear-gradient(180deg, rgba(255,255,255,0) 70%, rgba(127,179,212,0.35) 100%),
      linear-gradient(100deg, #dfe8ee 0%, var(--bench-grey) 30%, var(--white-coat) 55%, #eef2f5 80%, var(--bench-grey) 100%);
  }

  .inside-copy {
    padding: 12px 26px 8px;
    font-size: 9.5px;
    line-height: 12px;
  }
  .inside-copy p { margin-bottom: 6px; }
  .inside-copy h2 {
    font-size: 9.5px;
    font-weight: 700;
    margin-bottom: 1px;
  }
  .feature-list { list-style: none; margin-bottom: 6px; }
  .feature-list li { padding-left: 10px; position: relative; }
  .feature-list li::before {
    content: "";
    position: absolute;
    left: 0;
    top: 4px;
    width: 4px;
    height: 4px;
    border-radius: 50%;
    background: var(--ink);
  }

  .cover-contact {
    position: absolute;
    top: 470px;
    left: 0;
    width: 100%;
    text-align: center;
    font-size: 9px;
    line-height: 11.5px;
  }
  .brand-mark {
    display: block;
    width: 18px;
    height: 18px;
    margin: 0 auto 6px;
    border-radius: 50%;
    background: var(--accent);
  }
  .brand-name { font-weight: 700; }
</style>
</head>
<body>

  <section class="page page--inside">
    <div class="inside-top-band"></div>
    <div class="photo photo--tubes" role="img" aria-label="Photo of a rack of test tubes with green liquid held by a lab technician"></div>
    <div class="inside-copy">
      <p>Corvella Labs has been successfully serving North Dakota since 1996. Dr. Gavin Tellemy, President of Corvella Lab, has over 25 years of medical experience doing research for Brindle University and The University of Parkmoor. In addition, he has worked with clinics giving him a comprehensive understanding of drug testing. It is Corvella Lab mission to supply the best service for our customers by understanding their needs so they can provide the best possible patient care.</p>
      <h2>Corvella Features:</h2>
      <ul class="feature-list">
        <li>24 – 48 Hour Turnaround Time</li>
        <li>Customer Satisfaction is Our Number 1 Priority</li>
        <li>Capable of Billing all Major Insurance Companies</li>
        <li>Thorough Drug Testing Capabilities Including K2/Spice testing</li>
        <li>Apply Lean Process Control to Supply the best Quality of Analysis</li>
        <li>Easy and Convenient Web-based Interface</li>
        <li>Easy and Customizable Reporting</li>
        <li>The Vexlo is state of the art technology that uses ion entrapment to give better quantitative results. This gives us the ability to detect for more drugs at a higher accuracy.</li>
      </ul>
      <h2>Why test</h2>
      <p>Why Monitor Prescription Drug Usage? Prescription drug abuse is the use of medication without a prescription, in a way other than prescribed, or for the experience or feeling elicited. According to several national surveys, prescription medications, such as those used to treat pain, attention deficit disorders, and anxiety, are being abused at a rate second only to marijuana among illicit drug users. The consequences of this abuse have been steadily worsening, reflected in increased treatment admissions, emergency room visits, and overdose deaths.</p>
    </div>
    <div class="photo photo--office" role="img" aria-label="Photo of a smiling doctor speaking with a patient"></div>
  </section>

  <section class="page page--cover">
    <div class="photo photo--lab" role="img" aria-label="Photo of lab scientists in white coats working with pipettes, flasks and microscopes"></div>
    <div class="cover-contact">
      <span class="brand-mark"></span>
      <div class="brand-name">Corvella Diagnostics, Inc.</div>
      <div>482 Larkfield Ave. E</div>
      <div>Williston, ND 58934</div>
      <div>ph: (701) 555-0143</div>
      <div>www.corvellalab.test</div>
    </div>
  </section>

</body>
</html>
```